A5 Flyer for Christian Dating Agency for Church Notice Boards

Design brief
I write to tens of thousands of churches (of all denominations – ie Anglican, Methodist, Baptist, Evangelical, Catholic) every year and I send them an A5 flier to put up on their notice boards to ‘advertise’ or sign post the ‘single’ people (ie single never married, separated, divorced or widowed people) to my organisation ‘kindred7th’.
I’ve used a variety of designs in the past – and am now looking for a new design.
It’ll still be A5 and one sided.
It’ll be eye catching – it has to stand out on a notice board that probably has masses of other flyers/posters for all sorts of organisations/charities.
Vicars/church leaders will be happy to put it on their church notice board!
We have found in the past that using images of ‘happy couples’ is problematic – as people tend to identify with the pictures and then say “Well it’s obviously not for me as I’m not that colour, that age, etc” – or the images depict a certain type of person – that they aren’t – or they don’t fancy the person in the picture!
It needs to get across the very personal nature of our service – the fact that people aren’t a number or name on a database – but as members are known to us by name and we’ll get to know them through the course of their membership.
It needs to get across (probably by the professional great design) that we’re a professional organisation – not a cheap fly by night ‘just set up yesterday’ organisation. It needs to inspire confidence and trust because the people looking at it and thinking of contacting us will most likely never have done anything like this before (ie joined a dating agency) and in an ideal world would rather not have to!
So what I’m wanting is an A5 flyer that attracts and keeps peoples attention.
Within a very short space of time they will have realised we’re advertising a matchmaking/dating agency/organisation
They’ll get a sense of how we operate – and that we’re different to online sites
They feel comfortable and trusting of us
And most importantly they’ll be motivated to give us a call or look us up online.
Our telephone number is 0121 738 2961
Our web address is www.kindred7th.co.uk
*Background*
I run an OFF LINE Christian Dating and Introduction Agency. It’s off-line in that, although we have a website – which you’ll definitely want to have a look at to get a feel for our ‘brand’/ colour scheme etc as well as the flavour of who we are etc – we operate a totally off-line service. So we provide members details of other members by post and offer a very supportive service whereby my team and I are on the phone talking to, supporting, encouraging, listening, advising and helping members in any way we can to find their soul mate.
We’re a 100% stand alone Christian organisation. We only accept Christians onto our books – and Christians come to us because of that fact. They themselves are looking to meet other Christians who share their Christian faith.
We have members from late 20s right up to people in their 80s – and cater for all types of people – in terms of ethnicity, background, working life, location.
We are UK based and only cater for UK/Ireland members.
We charge a fee for our services – it’s an annual membership starting from £475 a year going up to £2127.
Everything we do is (we think!) different to online services and we like to set ourselves very apart from them. In our view (and this seems to be mirrored by the horror stories our members tell us of their experiences online) online sites are cheap to join, unreliable, full of non Christians (even if they say they are Christian sites), full of members that don’t really exist, full of people who aren’t really looking for a real friend or long term relationship (and this seems to be mirrored by the horror stories our members tell us of their experiences online).
We only want to attract Christians who are serious about finding new friends and companions and people who are looking to find a marriage partner long term.
We think we are the UK’s largest and most successful off line membership organisation (there’s no-one really doing what we’re doing – although we have lots of on-line competition).
We’ve been operating since 1999 and have had literally 100s of people get married through us – nearly 200 people in fact – and that’s only the ones we know about – we suspect there are many more.
We’re caring, professional, offer a raft of services like professional photo shoots, telephone coaching and materials to ensure that people don’t just get other members details but are successful in dating. (you can see our raft of services on our www.kindred7th.co.uk/join-now page)
You see the dating industry is littered with people NOT finding anyone – and it’s not because they aren’t eligible themselves but probably because they’re going about dating in the wrong way. It might seem the easiest thing in the world to do (because everyone’s doing it aren’t they?) whereas in fact it’s actually quite hard to do it right, to keep going after rejections and to find the right person for you. Everything we do is aimed to help people get it right and BE successful.
Reason: Would like to see amends to current designs as not yet fully decided which one to select and am awaiting changes
Target Market(s)
Single Christians - of all ages
Industry/Entity Type
Dating
Look and feel

```html
<!DOCTYPE html>
<html lang="en">
<head>
<meta charset="utf-8">
<title>kindred7th – Christian singles flyer</title>
<link href="https://fonts.googleapis.com/css2?family=Archivo+Black&family=Oswald:wght@600&family=Roboto:wght@400;500&family=Cabin:wght@400;600&display=swap" rel="stylesheet">
<style>
  :root{
    --navy:#2c5580;
    --heading-blue:#2d5f94;
    --icon-blue:#3f78b4;
    --sky:#1ea6dc;
    --ink:#1d1d1d;
    --white:#ffffff;
  }
  *{margin:0;padding:0;box-sizing:border-box}
  html,body{width:855px;height:1200px;overflow:hidden;background:var(--white)}
  .flyer{position:relative;width:855px;height:1200px;overflow:hidden;font-family:'Roboto',sans-serif;color:var(--ink)}
  .top-band{position:absolute;left:0;top:0;width:855px;height:86px;background:var(--navy);
    color:var(--white);font-family:'Roboto',sans-serif;font-weight:500;font-size:26.5px;letter-spacing:.3px;
    display:flex;align-items:center;justify-content:center}
  .hero{position:absolute;left:0;top:86px;width:855px;height:332px;
    background:linear-gradient(180deg,#2f5f6a 0%,#5e9a9a 30%,#9cc4bd 42%,#4b5a3a 50%,#3b3f38 70%,#2a2b29 100%)}
  .hero-caption{position:absolute;left:0;top:282px;width:855px;height:136px;background:rgba(20,20,20,.55);
    color:var(--white);text-align:center}
  .hero-title{font-family:'Archivo Black',sans-serif;font-size:48px;line-height:1;margin-top:16px;letter-spacing:.5px}
  .hero-sub{font-family:'Oswald',sans-serif;font-weight:600;font-size:27px;margin-top:14px;letter-spacing:.2px}
  .about{position:absolute;left:0;top:446px;width:326px;height:660px;background:var(--navy);color:var(--white);
    font-family:'Cabin',sans-serif}
  .about-frame{position:absolute;left:22px;top:27px;width:286px;height:511px;border:3px solid var(--white);padding:22px 0 0 20px}
  .about-frame h2{font-family:'Roboto',sans-serif;font-weight:500;font-size:35px;letter-spacing:-.5px;margin-bottom:6px}
  .about-frame p{font-size:15.8px;line-height:19.5px;margin-bottom:19px;padding-right:12px}
  .about-cta{position:absolute;left:0;top:566px;width:326px;text-align:center}
  .about-cta .lead{font-size:18.5px;font-weight:600}
  .about-cta .call{font-size:29px;margin-top:10px}
  .brand{position:absolute;left:466px;top:452px;display:flex;align-items:center;gap:8px;
    font-family:'Roboto',sans-serif;font-weight:500;font-size:36px;color:var(--navy)}
  .brand .dot{width:18px;height:18px;border-radius:50%;background:var(--navy)}
  .feature{position:absolute;left:480px;width:320px}
  .feature h3{font-weight:500;font-size:21px;color:var(--heading-blue);margin-bottom:16px;letter-spacing:.2px}
  .feature p{font-size:15.5px;line-height:19.2px}
  .icon{position:absolute}
  .contact{position:absolute;left:0;top:1106px;width:855px;height:94px;background:var(--sky);color:var(--white);
    display:flex;align-items:center;padding:0 0 8px 42px;font-family:'Cabin',sans-serif;font-weight:600}
  .contact .label{font-size:28px;margin-right:14px}
  .contact .item{display:flex;align-items:center;gap:6px;font-size:19px;margin-right:20px}
</style>
</head>
<body>
<div class="flyer">
  <header class="top-band">FINDING IT DIFFICULT TO MEET THE RIGHT PERSON?</header>

  <div class="hero" role="img" aria-label="Photograph of an open country road stretching to the horizon between grassy verges and water under a teal sky"></div>
  <div class="hero-caption">
    <h1 class="hero-title">Welcome to kindred7th</h1>
    <div class="hero-sub">- UK's largest OFFLINE Christian singles community -</div>
  </div>

  <section class="about">
    <div class="about-frame">
      <h2>ABOUT US</h2>
      <p>Founded in late 1999 by Margaret Ellison, kindred7th is an introduction service for single Christians across the UK.</p>
      <p>It is open to unattached Christians of all denominations and ages and welcomes people from a wide variety of backgrounds and traditions.</p>
      <p>The service is run on the simple basis of allowing people to make contact and friends with other people whose details they have seen and like the look of.</p>
      <p>We believe that friendships are vitally important and are at the heart of any good and meaningful relationship!</p>
    </div>
    <div class="about-cta">
      <div class="lead">Begin the next chapter of your life</div>
      <div class="call">Get in touch today!</div>
    </div>
  </section>

  <div class="brand"><span class="dot"></span>kindred7th</div>

  <svg class="icon" style="left:360px;top:520px" width="104" height="104" viewBox="0 0 104 104" aria-hidden="true">
    <circle cx="52" cy="50" r="44" fill="none" stroke="var(--icon-blue)" stroke-width="5"/>
    <circle cx="52" cy="50" r="32" fill="var(--icon-blue)"/>
  </svg>
  <div class="feature" style="top:526px">
    <h3>GENUINE MEMBERS</h3>
    <p>We only accept genuine Christians as members so if that’s what you’re looking for you’ll be in the right company with us.</p>
  </div>

  <svg class="icon" style="left:365px;top:686px" width="100" height="74" viewBox="0 0 100 74" aria-hidden="true">
    <rect x="2" y="2" width="96" height="70" fill="none" stroke="var(--icon-blue)" stroke-width="4"/>
    <polyline points="4,4 50,44 96,4" fill="none" stroke="var(--icon-blue)" stroke-width="4"/>
    <line x1="4" y1="70" x2="38" y2="34" stroke="var(--icon-blue)" stroke-width="4"/>
    <line x1="96" y1="70" x2="62" y2="34" stroke="var(--icon-blue)" stroke-width="4"/>
  </svg>
  <div class="feature" style="top:661px">
    <h3>OFF-LINE</h3>
    <p>Our membership and introduction service is provided entirely offline. A truly personal, interactive and effective way of meeting other single Christians.</p>
  </div>

  <svg class="icon" style="left:370px;top:828px" width="92" height="92" viewBox="0 0 92 92" aria-hidden="true">
    <circle cx="46" cy="46" r="42" fill="none" stroke="var(--navy)" stroke-width="5"/>
    <polyline points="46,16 46,46 30,66" fill="none" stroke="var(--navy)" stroke-width="5" stroke-linecap="round"/>
  </svg>
  <div class="feature" style="top:811px">
    <h3>COMMITMENT</h3>
    <p>You won’t find ‘here today, gone tomorrow’ members on our books. Just real genuine Christians who are truly committed to finding new friends and the right partner.</p>
  </div>

  <svg class="icon" style="left:376px;top:988px" width="90" height="90" viewBox="0 0 90 90" aria-hidden="true">
    <path d="M6 4 v16 l8 6 l8 -6 v-16 h6 v20 l-8 8 v50 a6 6 0 0 1 -12 0 v-50 l-8 -8 v-20 z" fill="none" stroke="var(--icon-blue)" stroke-width="3.5" stroke-linejoin="round"/>
    <circle cx="14" cy="80" r="2.5" fill="var(--icon-blue)"/>
    <rect x="46" y="4" width="30" height="14" rx="2" fill="var(--icon-blue)"/>
    <rect x="76" y="6" width="8" height="10" fill="var(--icon-blue)"/>
    <rect x="56" y="18" width="10" height="68" fill="none" stroke="var(--icon-blue)" stroke-width="3.5"/>
  </svg>
  <div class="feature" style="top:960px">
    <h3>EXPERT SUPPORT</h3>
    <p>We provide tools, education, coaching and support to make sure you’re doing the right things in the right way.  That’s what gets results!</p>
  </div>

  <footer class="contact">
    <span class="label">Contact us:</span>
    <span class="item">
      <svg width="18" height="18" viewBox="0 0 24 24" aria-hidden="true"><path d="M6.6 10.8a15 15 0 0 0 6.6 6.6l2.2-2.2a1 1 0 0 1 1-.25 11 11 0 0 0 3.6.6 1 1 0 0 1 1 1V20a1 1 0 0 1-1 1A17 17 0 0 1 3 4a1 1 0 0 1 1-1h3.5a1 1 0 0 1 1 1 11 11 0 0 0 .6 3.6 1 1 0 0 1-.25 1z" fill="none" stroke="#fff" stroke-width="2"/></svg>
      0121 738 2961</span>
    <span class="item">
      <svg width="26" height="18" viewBox="0 0 26 18" aria-hidden="true"><rect x="1" y="1" width="24" height="16" fill="none" stroke="#fff" stroke-width="2"/><polyline points="1,1 13,10 25,1" fill="none" stroke="#fff" stroke-width="2"/></svg>
      info@kindred7th.co.uk</span>
    <span class="item">
      <svg width="22" height="22" viewBox="0 0 22 22" aria-hidden="true"><g fill="none" stroke="#fff" stroke-width="1.6"><circle cx="11" cy="11" r="9.5"/><ellipse cx="11" cy="11" rx="4.5" ry="9.5"/><line x1="1.5" y1="11" x2="20.5" y2="11"/><line x1="3" y1="6" x2="19" y2="6"/><line x1="3" y1="16" x2="19" y2="16"/></g></svg>
      www.kindred7th.co.uk</span>
  </footer>
</div>
</body>
</html>
```